Vesta Power Web Design

I want a design for a home page that can function as a template for the entire web design. I"m also requesting that the design be adapted as a template for Power Point presentations, as well.

Here"s a brief about our company:

Vesta Power provides its customers with clean, redundant and reliable power. Functioning as a private power producer, Vesta Power owns and operates combined heat and power (CHP) and distributed generation (DG) systems.

Vesta’s management has extensive experience in aerospace turbines engine operation, maintenance, manufacturing and repair. Depending on the customer need, Vesta either builds new generators or refurbish “retired” aerospace turbines into industrial generators. This allows Vesta to deliver generating systems at greatly reduced capital outlays, enabling Vesta Power to offer its customers not only redundant power and grid independence, but significant savings on their energy needs. Vesta’s typical installation size is 500Kws to 3Mws but based upon our customer"s needs, Vesta can site multiple generators to configure systems of larger size.

By using aero derivative turbine engines the company has the flexibility to use the best source of fuel for each site and power requirement. The turbine engine can operate on virtually any combustible fuel. This allows Vesta to utilize the flex fuel practice and operate on either the least expensive fuel available or operate on renewable and biofuels to fulfill the green power requirements mandated by many federal, state and local utility commissions.

Vesta’s market strategy is as follows:

1. Sell reliable and redundant power through a PPAs or lease agreements to industrial or institutional customers with high electrical and thermal needs such as food processors, bio fuel producers, hospitals, casinos, hotels, etc.

2. Lease its systems to customer that “flare gas” as byproducts of their processes such as wastewater treatment facilities, land fills and "stranded gas wells" allowing them to use their waste products to power their facilities and sell excess electricity back to the grid.

3. Partner with other private power producers to provide the turbine generating capacity on a leased basis.
Updates

Please disregard the "turbine logo" that was uploaded as a file and focus only on the "bolt design logo", A (bolt) E.

We like the simple navigation and clean and modern design of sites.

http://www.plumvault.example/

http://www.serviqo.example/

http://www.trylumo.example/

Target Market(s)

Our target markets can be found on the web architecture file I've attached to this submission.

Number of Pages Required

1 page

Requirements
Must have
• The designer must provide a web design and a Power Point template based upon the web design.

• The design must contemplate the web architecture that I""ve included as a file.

```html
<!DOCTYPE html>
<html lang="en">
<head>
<meta charset="utf-8">
<title>Vesta Power</title>
<link rel="stylesheet" href="https://fonts.googleapis.com/css2?family=Ubuntu:wght@400;500&family=Tinos&display=swap">
<style>
:root{
  --green-deep:#3f9a5c;
  --green-bright:#7cc12f;
  --lime:#c6ec3a;
  --brand-text:#e8f7a8;
  --pale:#f7fbd0;
  --tab-text:#6a6a6a;
  --ink:#1a1a1a;
  --dash:#8a8f8a;
  --footer-band:#75866a;
  --tag-green:#8fe81a;
  --tag-red:#e8121a;
  --tag-orange:#f2622a;
}
*{box-sizing:border-box;margin:0;padding:0}
html,body{width:880px;height:1200px;overflow:hidden;background:#fff}
body{font-family:"Ubuntu",sans-serif;color:var(--ink);position:relative}
.header{position:absolute;left:0;top:0;width:880px;height:202px;
  background:radial-gradient(ellipse 60% 90% at 40% 30%,#49a66a 0%,transparent 70%),linear-gradient(100deg,var(--green-deep) 0%,#4aa55a 50%,var(--green-bright) 100%)}
.brand{position:absolute;left:0;width:880px;top:112px;text-align:center}
.brand-name{font-size:34px;font-weight:400;color:var(--brand-text);letter-spacing:.5px;display:inline-flex;align-items:center;gap:10px}
.brand-dot{width:14px;height:14px;border-radius:50%;background:var(--lime);display:inline-block}
.search{position:absolute;left:651px;top:166px;display:flex;align-items:center;gap:6px}
.search-field{width:123px;height:23px;border-radius:4px;background:#a8d678;border:1px solid #8cbf60}
.search-label{font-size:14px;color:#1e2a1e}
.nav{position:absolute;left:0;top:202px;width:880px;height:68px;background:linear-gradient(#f2f2f2,#dedede)}
.nav ul{list-style:none;display:flex}
.nav li{height:33px;background:linear-gradient(#f7f7f7,#dcdcdc);border:1px solid #c9c9c9;border-radius:3px 3px 0 0;
  font-size:16px;font-weight:500;color:var(--tab-text);display:flex;align-items:center;justify-content:center}
.page{position:absolute;left:0;top:270px;width:880px;height:806px;
  background:linear-gradient(90deg,#9fd565 0%,#e6f5b8 30%,var(--pale) 45%,#d4ec9a 70%,#8cc94a 100%)}
.panel-head{position:absolute;left:15px;width:217px;height:60px;border:1px solid #b8c8a8;
  display:flex;align-items:center;justify-content:center;font-size:18px;font-weight:500}
.panel-head.testimonials{top:25px;background:linear-gradient(#fff,#c4e88a)}
.panel-head.news{top:275px;background:linear-gradient(#fff,#d8d8d8)}
.panel-body{position:absolute;left:15px;width:217px;border:1px solid #b8c8a8;border-top:none;
  padding:10px 10px;font-size:13.5px;line-height:24px;text-align:justify;background:rgba(255,255,255,.15)}
.panel-body.testimonials{top:85px;height:183px}
.panel-body.news{top:335px;height:195px}
.title-bar{position:absolute;left:241px;width:627px;background:linear-gradient(90deg,#fbfcdc,#f4f7a8);
  font-weight:400;padding-left:15px;display:flex;align-items:center}
.title-bar.headline{top:25px;height:47px;font-size:29px}
.title-bar.updates{top:456px;height:71px;font-size:32px}
.article{position:absolute;left:241px;top:75px;width:627px;height:369px;border:2px dashed var(--dash);
  padding:18px 15px;font-size:13px;line-height:24px;text-align:justify}
.article p{text-indent:120px;margin-bottom:8px}
.cards{position:absolute;left:14px;top:536px;width:855px;height:244px;display:flex;gap:3px}
.card{flex:1;border:2px dashed var(--dash);padding:6px;position:relative}
.card-media{width:100%;height:100%;border:1px dashed #999}
.media-team{background:linear-gradient(#fff,#eee 70%,#fff)}
.media-pair{background:linear-gradient(90deg,#b9b9b9,#d5d5d5 55%,#efefef)}
.media-deal{background:radial-gradient(ellipse at 40% 30%,#c8603a,#8a2010 80%)}
.tag{position:absolute;top:178px;right:22px;height:24px;padding:0 16px 0 12px;font-size:11px;color:#fff;
  display:flex;align-items:center;clip-path:polygon(0 0,88% 0,100% 50%,88% 100%,0 100%)}
.tag.green{background:var(--tag-green)}
.tag.red{background:var(--tag-red)}
.tag.orange{background:var(--tag-orange)}
.footer{position:absolute;left:0;top:1076px;width:880px;height:100px;background:#fff}
.copyright{position:absolute;left:0;width:880px;top:74px;text-align:center;font-family:"Tinos",serif;font-size:13px}
.trust-badge{position:absolute;left:716px;top:34px;width:108px;height:36px;border-radius:4px;background:#d9dde3}
.footer-band{position:absolute;left:0;top:1176px;width:880px;height:24px;background:var(--footer-band)}
</style>
</head>
<body>
<header class="header">
  <div class="brand">
    <div class="brand-name"><span class="brand-dot"></span>Vesta Power</div>
  </div>
  <div class="search"><div class="search-field"></div><span class="search-label">Search</span></div>
</header>
<nav class="nav">
  <ul>
    <li style="width:146px">About Vesta</li>
    <li style="width:110px">CHP</li>
    <li style="width:146px">Stranded Gas</li>
    <li style="width:146px">Resources</li>
    <li style="width:182px">Partners &amp; Suppliers</li>
    <li style="width:150px">Contact us</li>
  </ul>
</nav>
<main class="page">
  <div class="panel-head testimonials">Testimonials</div>
  <div class="panel-body testimonials">Vesta Power provides its customers with clean, redundant and reliable power. Functioning as a private power producer, Vesta Power owns and operates</div>
  <div class="panel-head news">News</div>
  <div class="panel-body news">Vesta Power provides its customers with clean, redundant and reliable power. Functioning as a private power producer, Vesta Power owns and operates combined heat and power (CHP)</div>

  <h1 class="title-bar headline">Headline</h1>
  <article class="article">
    <p>Vesta Power provides its customers with clean, redundant and reliable power. Functioning as a private power producer, Vesta Power owns and operates combined heat and power (CHP) and distributed generation (DG) systems.</p>
    <p>Vesta’s management has extensive experience in aerospace turbines engine operation, maintenance, manufacturing and repair. Depending on the customer need, Vesta either builds new generators or refurbish “retired” aerospace turbines into industrial generators. This allows Vesta to</p>
  </article>

  <h2 class="title-bar updates">Recent updates</h2>
  <section class="cards">
    <div class="card"><div class="card-media media-team" role="img" aria-label="Photo of a business team standing together"></div><span class="tag green">READ MORE</span></div>
    <div class="card"><div class="card-media media-pair" role="img" aria-label="Photo of two business colleagues in suits"></div><span class="tag red">READ MORE</span></div>
    <div class="card"><div class="card-media media-deal" role="img" aria-label="Photo of a business handshake"></div><span class="tag orange">READ MORE</span></div>
  </section>
</main>
<footer class="footer">
  <div class="trust-badge" role="img" aria-label="Security certificate badge"></div>
  <div class="copyright">All rights reserved Vesta Power 2010</div>
</footer>
<div class="footer-band"></div>
</body>
</html>
```